NEW Modern Sleek Business Card for VR Language Startup

Our startup is using VR to lead the next wave of world language education. We need a two-sided business card that introduces the larger organization (Quorvel Language Inc) and our contact info on one side and shows the product, Lumidrasca, on the other side.

Side 1 (contact info)= Quorvel Logo and Contact info (name, title, phone, email)

Side 2 (product)= Lumidrasc logo, text, and website
Text= Culturally Immersive Language Learning Games
Website= www.lumidrasc.example

Target Market(s)

Education, Technology

Contact Information for Business Card

Contact info will be updated upon approval of the design. For now, put this as a placeholder.

Perry Hollins
Founder & CEO
phollins@mailtrove.example
(555)-014-2736

Font styles to use
Other font styles liked:
• Gibson and Century Gothic are the brand fonts

Requirements
Nice to have
• I would love to see cohesion between the design and colors of the two logos. I have attached a few business card designs that I like, so you can get a feel for my preferred style.

```html
<!DOCTYPE html>
<html lang="en">
<head>
<meta charset="utf-8">
<title>Quorvel Language – Business Card</title>
<link rel="stylesheet" href="https://fonts.googleapis.com/css2?family=Questrial&family=Didact+Gothic&display=swap">
<style>
  :root {
    --page: #ffffff;
    --card: #1e1f1f;
    --accent: #5b84c4;
    --text-light: #d2d2d2;
    --text-white: #ffffff;
    --text-muted: #8a8a8a;
    --shade: #2a2a2a;
  }
  * { box-sizing: border-box; margin: 0; padding: 0; }
  html, body {
    width: 1031px;
    height: 1200px;
    overflow: hidden;
    background: var(--page);
  }
  .card {
    position: absolute;
    width: 963px;
    height: 550px;
    background: var(--card);
    overflow: hidden;
    font-family: "Didact Gothic", "Questrial", sans-serif;
  }
  .card--front {
    left: 34px;
    top: 34px;
    border-left: 14px solid var(--accent);
    border-bottom: 14px solid var(--accent);
  }
  .card--back {
    left: 33px;
    top: 619px;
    border-right: 14px solid var(--accent);
    border-bottom: 14px solid var(--accent);
  }
  .card__shade {
    position: absolute;
    border-radius: 50%;
  }
  .card--front .card__shade {
    right: -90px;
    top: -110px;
    width: 380px;
    height: 380px;
    background: radial-gradient(circle at 45% 45%, var(--shade) 0%, var(--shade) 55%, rgba(42,42,42,0) 72%);
  }
  .card--back .card__shade {
    left: -120px;
    bottom: -110px;
    width: 400px;
    height: 400px;
    background: radial-gradient(circle at 55% 55%, var(--shade) 0%, var(--shade) 55%, rgba(42,42,42,0) 72%);
  }

  /* Front: company mark */
  .brand {
    position: absolute;
    display: flex;
    align-items: center;
    gap: 26px;
  }
  .brand__dot {
    border-radius: 50%;
    background: var(--accent);
  }
  .brand__name {
    font-family: "Questrial", sans-serif;
    font-weight: 400;
    line-height: 1;
  }
  .card--front .brand { left: 50px; top: 72px; }
  .card--front .brand__dot { width: 100px; height: 100px; }
  .card--front .brand__name {
    font-size: 62px;
    letter-spacing: 8px;
    color: var(--text-white);
  }

  /* Front: person */
  .person {
    position: absolute;
    left: 42px;
    top: 318px;
  }
  .person__name {
    font-family: "Questrial", sans-serif;
    font-size: 56px;
    font-weight: 400;
    color: var(--accent);
    line-height: 1.1;
  }
  .person__title {
    margin-top: 18px;
    font-size: 24px;
    letter-spacing: 2.5px;
    color: var(--text-light);
  }

  /* Front: contact */
  .contact {
    position: absolute;
    right: 34px;
    top: 333px;
    list-style: none;
  }
  .contact__item {
    display: flex;
    align-items: center;
    justify-content: flex-end;
    gap: 36px;
    height: 36px;
    margin-bottom: 24px;
    font-size: 23px;
    letter-spacing: 2px;
    color: var(--text-light);
  }
  .contact__icon {
    width: 34px;
    height: 34px;
    flex: none;
  }

  /* Back: product mark */
  .card--back .brand {
    right: 40px;
    top: 80px;
    flex-direction: column;
    align-items: flex-end;
    gap: 22px;
  }
  .card--back .brand__dot { width: 120px; height: 120px; margin-right: 40px; }
  .card--back .brand__name {
    font-size: 44px;
    color: var(--text-muted);
  }

  /* Back: tagline */
  .product-info {
    position: absolute;
    right: 36px;
    top: 403px;
    width: 680px;
  }
  .product-info__row {
    display: flex;
    align-items: center;
    justify-content: flex-end;
    gap: 30px;
  }
  .product-info__rule {
    flex: 1;
    height: 16px;
  }
  .product-info__url {
    font-size: 26px;
    color: var(--text-light);
    letter-spacing: 0.5px;
    white-space: nowrap;
  }
  .product-info__url-domain { color: var(--accent); }
  .product-info__tagline {
    margin-top: 20px;
    text-align: right;
    font-size: 26px;
    color: var(--text-light);
    letter-spacing: 0.3px;
  }
</style>
</head>
<body>

  <section class="card card--front" aria-label="Business card front">
    <div class="card__shade" role="img" aria-label="Faint background brand decoration"></div>

    <div class="brand">
      <span class="brand__dot" aria-hidden="true"></span>
      <span class="brand__name">Quorvel</span>
    </div>

    <div class="person">
      <h1 class="person__name">Perry Hollins</h1>
      <p class="person__title">Founder &nbsp;|&nbsp; CEO</p>
    </div>

    <ul class="contact">
      <li class="contact__item">
        <span>(555)-014-2736</span>
        <svg class="contact__icon" viewBox="0 0 24 24" aria-hidden="true">
          <path d="M6.6 2.5c.6-.3 1.2-.1 1.5.4l2 3.3c.3.5.2 1.1-.2 1.5L8.4 9c.9 2.6 3.9 5.8 6.6 6.8l1.3-1.4c.4-.4 1-.5 1.5-.2l3.3 1.9c.5.3.7 1 .4 1.5l-1 1.8c-.5.9-1.6 1.4-2.7 1.1C11.5 19 5.4 12.8 4 6.5c-.3-1.1.2-2.2 1.1-2.7z" fill="none" stroke="#5b84c4" stroke-width="1.6" stroke-linejoin="round"/>
        </svg>
      </li>
      <li class="contact__item">
        <span>phollins@mailtrove.example</span>
        <svg class="contact__icon" viewBox="0 0 24 24" aria-hidden="true">
          <path d="M2.5 6h19v1.8l-9.5 5.6-9.5-5.6z" fill="#5b84c4"/>
          <path d="M2.5 10l9.5 5.6 9.5-5.6V19h-19z" fill="#5b84c4"/>
        </svg>
      </li>
    </ul>
  </section>

  <section class="card card--back" aria-label="Business card back">
    <div class="card__shade" role="img" aria-label="Faint background brand decoration"></div>

    <div class="brand">
      <span class="brand__dot" aria-hidden="true"></span>
      <span class="brand__name">Lumidrasc</span>
    </div>

    <div class="product-info">
      <div class="product-info__row">
        <svg class="product-info__rule" viewBox="0 0 330 16" preserveAspectRatio="none" aria-hidden="true">
          <circle cx="8" cy="8" r="6" fill="none" stroke="#5b84c4" stroke-width="2.5"/>
          <line x1="14" y1="8" x2="330" y2="8" stroke="#5b84c4" stroke-width="3"/>
        </svg>
        <span class="product-info__url">www.<span class="product-info__url-domain">lumidrasc</span>.example</span>
      </div>
      <p class="product-info__tagline">Culturally Immersive Language Learning Games</p>
    </div>
  </section>

</body>
</html>
```